**** Business card design for VoltaNode ****

For my ICT company VoltaNode I need I need a business card design.

We design, build and host web-applications and we have our own CMS product.

Some good examples are attached.

The information should be:
Joris Tielenburg
Managing director
E: j.tielenburg@voltanode-example.nl
M: +31(0)6 57218064
T: +31(0)40 7249305
W: www.voltanode-example.nl

Address:
Berend Vlootweg 27
5612 KT Eindhoven

Industry/Entity Type

Business

Requirements
Must have
• - Use logo (see attachments)
- Double sided
- Distinctive
Nice to have
• - Place for a statement on the back-side: "Designed with knowledge, built with passion"
- HTML code (or Wordpress)
- Dark (black or dark-gray) side
- Small simple images for telephone, e-mail en Url.
- QR code (only if not disturbing), not required, just an option

```html
<!DOCTYPE html>
<html lang="en">
<head>
<meta charset="utf-8">
<title>VoltaNode – Business Card</title>
<link rel="stylesheet" href="https://fonts.googleapis.com/css2?family=Source+Sans+3:wght@400;600&display=swap">
<style>
  :root {
    --page-bg: #1c1d1f;
    --card-bg: #0d0f11;
    --card-edge: #3b3d41;
    --text-main: #f2f4f6;
    --text-soft: #d6d9dd;
    --accent: #3a8fd8;
    --rule: #8a8d92;
  }
  * { margin: 0; padding: 0; box-sizing: border-box; }
  html, body {
    width: 1200px; height: 800px; overflow: hidden;
    background: var(--page-bg);
    font-family: "Source Sans 3", "Myriad Pro", Arial, sans-serif;
  }
  .canvas { position: relative; width: 1200px; height: 800px; }

  .card {
    position: absolute;
    background: var(--card-bg);
    border: 1px solid var(--card-edge);
    border-radius: 19px;
    overflow: hidden;
  }
  .card--back  { left: 506px; top: 370px; width: 682px; height: 416px; }
  .card--front { left: 17px;  top: 20px;  width: 677px; height: 414px; }

  .rule {
    position: absolute; height: 2px;
  }
  .rule--fade-right { background: linear-gradient(90deg, var(--rule), rgba(138,141,146,0)); }
  .rule--fade-left  { background: linear-gradient(90deg, rgba(138,141,146,0), var(--rule)); }

  .brand {
    position: absolute;
    display: flex; align-items: center; gap: 10px;
    color: var(--accent);
    font-weight: 600;
    letter-spacing: 0.5px;
  }
  .brand__mark { background: var(--accent); flex: none; }
  .card--front .brand { left: 482px; top: 108px; font-size: 30px; }
  .card--front .brand__mark { width: 16px; height: 16px; }
  .card--back .brand { left: 0; right: 0; top: 138px; justify-content: center; font-size: 46px; }
  .card--back .brand__mark { width: 22px; height: 22px; }

  .person { position: absolute; left: 8px; top: 272px; }
  .person__name { font-size: 19px; color: var(--text-main); font-weight: 400; line-height: 1.1; }
  .person__surname { color: var(--accent); }
  .person__role { font-size: 11.5px; color: var(--text-soft); margin-top: 3px; }

  .contact { position: absolute; left: 6px; top: 320px; list-style: none; }
  .contact__item {
    display: flex; align-items: flex-start; gap: 8px;
    font-size: 11.5px; color: var(--text-soft); line-height: 1.3;
  }
  .contact__item + .contact__item { margin-top: 9px; }
  .contact__icon { width: 14px; height: 14px; flex: none; margin-top: 1px; }

  .address { position: absolute; right: 8px; top: 342px; text-align: right; }
  .address__title { font-size: 20px; color: var(--accent); line-height: 1.1; }
  .address__line { font-size: 11.5px; color: var(--text-soft); line-height: 1.35; }

  .tagline {
    position: absolute; left: 0; right: 0; top: 340px;
    text-align: center; font-size: 19px; color: var(--text-main);
  }
</style>
</head>
<body>
<main class="canvas">

  <section class="card card--back" aria-label="Card back">
    <div class="brand"><span class="brand__mark"></span>VoltaNode</div>
    <div class="rule rule--fade-left" style="left:550px; right:0; top:329px;"></div>
    <p class="tagline">Designed with knowledge, built with passion</p>
  </section>

  <section class="card card--front" aria-label="Card front">
    <div class="brand"><span class="brand__mark"></span>VoltaNode</div>

    <div class="rule rule--fade-right" style="left:0; width:130px; top:248px;"></div>
    <div class="rule rule--fade-left" style="left:547px; right:0; top:326px;"></div>

    <div class="person">
      <p class="person__name">Joris <span class="person__surname">Tielenburg</span></p>
      <p class="person__role">Managing Director</p>
    </div>

    <ul class="contact">
      <li class="contact__item">
        <svg class="contact__icon" viewBox="0 0 14 14" aria-hidden="true">
          <path d="M3 1.5 L5 1.5 L5.8 4.2 L4.4 5.3 C5.1 7 6.6 8.6 8.5 9.5 L9.6 8.1 L12.3 9 L12.3 11 C12.3 11.8 11.6 12.5 10.8 12.4 C6 11.9 2 7.9 1.6 3.1 C1.5 2.2 2.2 1.5 3 1.5 Z" fill="#3a8fd8"/>
        </svg>
        <span>M: +31(0)6 57218064<br>T: +31(0)40 7249305</span>
      </li>
      <li class="contact__item">
        <svg class="contact__icon" viewBox="0 0 14 14" aria-hidden="true">
          <g fill="none" stroke="#3a8fd8" stroke-width="1.1">
            <circle cx="7" cy="7" r="5.5"/>
            <ellipse cx="7" cy="7" rx="2.4" ry="5.5"/>
            <line x1="1.5" y1="7" x2="12.5" y2="7"/>
          </g>
        </svg>
        <span>j.tielenburg@voltanode-example.nl</span>
      </li>
      <li class="contact__item">
        <svg class="contact__icon" viewBox="0 0 14 14" aria-hidden="true">
          <g fill="none" stroke="#3a8fd8" stroke-width="1.1">
            <rect x="1.5" y="3" width="11" height="8" rx="1"/>
            <polyline points="1.5,3.5 7,8 12.5,3.5"/>
          </g>
        </svg>
        <span>www.voltanode-example.nl</span>
      </li>
    </ul>

    <div class="address">
      <p class="address__title">Address</p>
      <p class="address__line">Berend Vlootweg 27</p>
      <p class="address__line">5612 KT Eindhoven</p>
    </div>
  </section>

</main>
</body>
</html>
```